Presentation for Design Industry

Halvorsen Custom Plastics & Acrylics is a custom plastic design/build company based in Canada that actively collaborates with Architects, Designers and Builders.
The versatility and economic attractiveness of plastics has engendered a renaissance in the use of this material in all aspects for our wide client base. We have changed our company from being a custom manufacturer. We are now embracing the opportunity to be part of the design process and contribute\ing unique design features using leading edge approaches and materials.
We would like our presentation to highlight this new design aspect of our company. One of our partners is www.vantelux-panels.example ~ this particular website outlines much of what we do and can be used as an example for design focussed towards our same target market. We are looking for a high-end, original presentation. If the design and concept is good, there are opportunities to be involved in our new website build within the next month.
A loose outline of our presentation is uploaded for your reference. Our brochures and graphics files are also available for your reference.
Adobe Acrobat Presentation*, PowerPoint or Google Presentation
http://halvorsenplastics.example/interior-industrial-design.htm
https://files.example.net/sh/bx4kw7rmt2n9cfa/Rpln52ke3q
Updates
Thank you to all who worked on submitting your designs based on a vague but necessary description. We were looking for something to pop out at us...not knowing exactly what we wanted we needed a design concept to emerge from the information we were able to provide. Perhaps this needed some entrepreneurial thought process or marketing experience behind the design concept. You all had great ideas. Thank you again for all your hard work and creativity!
Target Market(s)
Interior Designers; Architects; Environmental Designer, Building Contractors, Retail Designers
Industry/Entity Type
Plastic
Look and feel
Each slider illustrates characteristics of the customer's brand and the style your logo design should communicate.

```html
<!DOCTYPE html>
<html lang="en">
<head>
<meta charset="utf-8">
<title>Halvorsen – New Range Product 2015</title>
<link rel="stylesheet" href="https://fonts.googleapis.com/css2?family=Open+Sans:wght@400&display=swap">
<style>
  :root {
    --stage: #000000;
    --paper: #ffffff;
    --title-red: #c0504d;
    --accent-orange: #e46c0a;
    --subtitle-grey: #7f7f7f;
    --body-ink: #1a1a1a;
    --brand-ink: #595959;
    --panel-blue: #6fa8dc;
    --panel-frost: #d9dee3;
    --heat-red: #c3262b;
    --heat-steel: #9aa0a6;
  }
  * { box-sizing: border-box; margin: 0; padding: 0; }
  html, body {
    width: 1200px; height: 378px; overflow: hidden;
    background: var(--stage);
    font-family: "Open Sans", Verdana, sans-serif;
  }
  .slide {
    position: absolute; top: 10px; height: 358px;
    background: var(--paper); overflow: hidden;
  }
  .slide--title { left: 62px; width: 495px; }
  .slide--values { left: 622px; width: 481px; }

  .photo { position: absolute; display: block; }
  .photo--panels {
    left: 0; top: 0; width: 290px; height: 358px;
    background: linear-gradient(160deg, var(--panel-blue) 0%, var(--panel-frost) 45%, #eef1f3 70%, var(--panel-blue) 100%);
  }
  .photo--heater {
    left: 0; top: 127px; width: 481px; height: 231px;
    background: linear-gradient(100deg, #e9ecef 0%, var(--heat-red) 30%, #8d1a1e 55%, var(--heat-steel) 80%, #cfd3d6 100%);
  }

  .title-box {
    position: absolute; left: 175px; top: 75px; width: 320px; height: 103px;
    background: var(--paper); padding-right: 30px;
    display: flex; align-items: center; justify-content: center;
  }
  .title-box h1 {
    font-weight: 400; font-size: 36px; line-height: 40px;
    color: var(--title-red); text-align: center;
  }
  .subtitle-box {
    position: absolute; left: 268px; top: 225px; width: 227px; height: 60px;
    background: var(--paper); padding-right: 30px;
    display: flex; align-items: center; justify-content: center;
  }
  .subtitle-box p {
    font-size: 19px; line-height: 25px; color: var(--subtitle-grey); text-align: center;
  }

  .brand {
    position: absolute; top: 330px; height: 24px;
    background: var(--paper);
    display: flex; align-items: center; padding: 0 5px;
    font-size: 11px; font-weight: 400; color: var(--brand-ink);
  }
  .slide--title .brand { left: 212px; }
  .slide--values .brand { left: 196px; }

  .values-heading {
    position: absolute; left: 21px; top: 38px;
    font-weight: 400; font-size: 27.5px; line-height: 32px;
    color: var(--accent-orange);
  }
  .values-box {
    position: absolute; left: 193px; top: 45px; width: 250px; height: 238px;
    background: var(--paper); padding: 4px 0 0 0;
  }
  .values-list { list-style: none; }
  .values-list li {
    position: relative; padding-left: 21px; margin-bottom: 3px;
    font-size: 15.5px; line-height: 20px; color: var(--body-ink);
    white-space: nowrap;
  }
  .values-list li::before {
    content: ""; position: absolute; left: 6px; top: 8px;
    width: 5px; height: 5px; background: var(--accent-orange);
  }
</style>
</head>
<body>

<section class="slide slide--title">
  <div class="photo photo--panels" role="img" aria-label="Photograph of interlocking translucent blue, green and frosted acrylic panels"></div>
  <div class="title-box"><h1>New Range<br>Product 2015</h1></div>
  <div class="subtitle-box"><p>Main title<br>presentation</p></div>
  <div class="brand">Halvorsen</div>
</section>

<section class="slide slide--values">
  <div class="photo photo--heater" role="img" aria-label="Close-up photograph of red wave-formed plastic sheet glowing under heating elements"></div>
  <h2 class="values-heading">Our Values</h2>
  <div class="values-box">
    <ul class="values-list">
      <li>Appreciate and share profits<br>with employees.</li>
      <li>Quality as a result of<br>continuous improvement<br>(get a little better every<br>day).</li>
      <li>Professionalism and<br>integrity in everything we<br>do.</li>
      <li>Guard our reputation<br>ruthlessly.Text</li>
    </ul>
  </div>
  <div class="brand">Halvorsen</div>
</section>

</body>
</html>
```